Norvale Code Builders Summit

We need a web design for a new brand of annual software development conference hosted in Riga, Latvia. Previously we used this page http://brimtorfest.lv/ and we also have a small concept over here http://www.brimtorfest.tk/. It is possible to view the content from past years there. It will not change radically next year.

Due to organisational changes we are rebranding the conference to 'Tolvik Code Meet' therefore we need a new web site and logo. Logo could be just 'TOLVIK CODE MEET' letters with proper font and font color selected, but if you like you could go creative. We also have a mobile app, which will be branded according to the designed web site afterwards. This is purely software development conference, so the web site visitors are techies. It will contain standard conference information such as schedule, speakers info, announcements, photos etc. The intention of this project is to create a design, which would attract people by ensuring that content quality would be on a high level.

The design should be modern, simple and without clutter. The design is intended to be responsive. The entry location should make accent on the conference date (22 of January, 2015) and some kind of short slogan (5-6 words max). Page should have initial wow effect for technical geeks.

Conference is organised by several local user groups (PKO Latvia, WMB Riga, TRZAP). Logos are attached. These are organisers, not sponsors.

One of the examples of something similar to what we would like to have http://www.quorvenfest.org/
Updates

Payment is now guaranteed in this project.

Target Market(s)

Software developers

Industry/Entity Type

Software

Requirements
Must have
• Should say TOLVIK CODE MEET as a main title.
Modern looking.
Shows conference speakers with their photos.
Presents conference schedule in 4-5 parallel tracks.
Place to put organisers an sponsors logos.
Social network promotion buttons.
Nice to have
• Parallax scrolling design.
Nice background using photos from previous events (https://pics.velmorashare.com/photos/+oswintharle/albums/7392018465527104816, https://pics.velmorashare.com/u/1/photos/302957184620473918264/albums/8163027594410273925)
Integrated Chirplex feed.
Should not have
• Photos of unrelated people.
Cliche photos and pictures.
Orange color as main one.

```html
<!DOCTYPE html>
<html lang="en">
<head>
<meta charset="utf-8">
<title>Tolvik Code Meet</title>
<link rel="stylesheet" href="https://fonts.googleapis.com/css2?family=Josefin+Sans:wght@600;700&family=Questrial&display=swap">
<style>
:root{
  --yellow:#ebe81c;
  --black:#0b0b0b;
  --ink:#222;
  --muted:#8a8a8a;
  --light:#f4f4f4;
  --line:#e2e2e2;
  --white:#fff;
}
*{box-sizing:border-box;margin:0;padding:0}
html,body{width:1200px;height:2927px;overflow:hidden}
body{position:relative;background:var(--white);font-family:"Questrial",sans-serif;color:var(--ink)}
.abs{position:absolute}
.head{font-family:"Josefin Sans",sans-serif;font-weight:700;text-transform:uppercase;color:var(--ink)}
.section-title{position:absolute;left:0;width:1200px;text-align:center;font-size:17px;letter-spacing:.5px}

/* hero */
.hero{position:absolute;left:0;top:0;width:1200px;height:597px;background:radial-gradient(ellipse at 60% 55%,#4a4038 0%,#231d18 45%,#0c0b0a 100%)}
.hero-photo{position:absolute;inset:0}
.brand{position:absolute;left:132px;top:46px;display:flex;align-items:center;gap:10px;color:var(--white);font-family:"Josefin Sans",sans-serif;font-weight:700;font-size:26px}
.brand-dot{width:18px;height:18px;border-radius:50%;background:var(--yellow)}
.btn-top{position:absolute;top:27px;height:41px;border:1px solid var(--white);color:var(--white);font-family:"Josefin Sans",sans-serif;font-weight:600;font-size:14px;display:flex;align-items:center;justify-content:center;text-transform:uppercase}
.btn-top.register{border-color:var(--yellow);color:var(--yellow)}
.nav{position:absolute;top:108px;right:130px;display:flex;gap:0}
.nav a{color:var(--white);text-decoration:none;font-family:"Josefin Sans",sans-serif;font-weight:600;font-size:14px;text-transform:uppercase}
.dots{position:absolute;top:434px;left:993px;display:flex;gap:11px}
.dots span{width:18px;height:18px;border-radius:50%;border:3px solid var(--white)}
.dots span.on{border-color:var(--yellow)}
.countdown{position:absolute;left:131px;top:474px;width:275px;height:106px;background:var(--yellow);display:flex;justify-content:space-around;align-items:center;text-align:center;font-family:"Josefin Sans",sans-serif;font-weight:700;font-size:17px;line-height:1.45;color:var(--ink)}
.welcome{position:absolute;left:425px;top:474px;width:644px;height:106px;background:#ececec;padding:14px 22px}
.welcome h1{font-size:17px;margin-bottom:10px}
.welcome p{font-size:12px;line-height:19px;color:#666}

/* news */
.news-item{position:absolute;left:131px;width:240px;height:72px}
.date{position:absolute;left:0;top:0;width:74px;height:72px;border:1px solid var(--line);background:var(--white);text-align:center}
.date b{display:block;font-family:"Josefin Sans",sans-serif;font-size:26px;padding-top:11px;height:45px}
.date i{display:block;font-style:normal;background:var(--yellow);font-family:"Josefin Sans",sans-serif;font-weight:700;font-size:10px;height:25px;line-height:26px}
.news-item p{position:absolute;left:86px;top:2px;width:150px;font-size:11.5px;line-height:17px;color:var(--muted)}
.arrows{position:absolute;top:637px;left:1030px;display:flex;gap:4px}
.arrows span{width:17px;height:17px;border-radius:50%;background:#bbb}
.arrows span:last-child{background:#555}
.card{position:absolute;top:673px;width:308px}
.card .pic{height:197px}
.card h4{margin-top:22px;font-size:12.5px;font-family:"Josefin Sans",sans-serif;font-weight:600}
.card h5{margin-top:7px;font-size:12.5px;font-family:"Josefin Sans",sans-serif;font-weight:700;text-transform:uppercase}
.card p{margin-top:14px;font-size:12px;line-height:19px;color:#666}
.btn-yellow{display:inline-flex;margin-top:14px;width:129px;height:37px;background:var(--yellow);align-items:center;justify-content:center;font-family:"Josefin Sans",sans-serif;font-weight:700;font-size:12px;text-transform:uppercase}

/* schedule */
.schedule{position:absolute;left:0;top:1093px;width:1200px;height:575px;background:var(--light)}
.tabs{position:absolute;left:291px;top:103px;display:flex;height:51px;border:1px solid var(--line);background:var(--white)}
.tabs span{display:flex;align-items:center;padding:0 20px;font-family:"Josefin Sans",sans-serif;font-weight:600;font-size:12.5px;text-transform:uppercase;border-right:1px solid var(--line)}
.tabs span:last-child{border-right:0}
.tabs span.on{background:#3a3a3a;color:var(--white)}
.timeline{position:absolute;left:270px;top:179px;width:4px;height:343px;background:var(--white)}
.time{position:absolute;left:131px;width:138px;height:36px;background:var(--yellow);font-size:11px;display:flex;align-items:center;justify-content:center}
.knob{position:absolute;left:264px;width:12px;height:12px;border-radius:50%;border:2px solid #ccc;background:var(--white)}
.slot{position:absolute;left:293px;width:776px;background:var(--white);border-left:4px solid var(--yellow);box-shadow:0 1px 3px rgba(0,0,0,.08)}
.slot h4{font-family:"Josefin Sans",sans-serif;font-weight:600;font-size:12.5px;text-transform:uppercase;padding:22px 0 0 28px}
.slot .org{position:absolute;left:28px;top:56px;width:66px;height:66px;border:1px solid var(--line);display:flex;align-items:center;justify-content:center;font-family:"Josefin Sans",sans-serif;font-weight:700;font-size:11px}
.slot p{position:absolute;left:122px;top:60px;width:620px;font-size:12px;line-height:24px;color:#999}

/* speakers */
.speaker{position:absolute;top:1766px;width:203px;height:283px;border:1px solid var(--line);border-bottom:5px solid var(--yellow);text-align:center;background:var(--white)}
.speaker.active{background:var(--yellow)}
.speaker .face{width:94px;height:94px;margin:26px auto 0;background:linear-gradient(160deg,#a27a60,#5b4538)}
.speaker h4{margin-top:40px;font-family:"Josefin Sans",sans-serif;font-weight:700;font-size:13px}
.speaker p{margin:10px auto 0;width:170px;font-size:11px;line-height:15px;color:#555}
.social{display:flex;justify-content:center;gap:14px;margin-top:14px}
.social span{width:13px;height:13px;border-radius:50%;background:#333}
.side-arrow{position:absolute;top:1886px;width:18px;height:18px;border-radius:50%;background:#aaa}

/* photos */
.photos{position:absolute;left:0;top:2103px;width:1200px;height:379px;background:var(--light)}
.pill{position:absolute;height:26px;border:1px solid var(--line);background:var(--white);font-size:11px;display:flex;align-items:center;padding:0 9px;font-family:"Josefin Sans",sans-serif;font-weight:600}
.photo{position:absolute;top:111px;width:230px;height:186px}

/* sponsors */
.sponsor{position:absolute;top:2575px;height:40px;display:flex;align-items:center;font-family:"Josefin Sans",sans-serif;font-weight:700;font-size:25px;color:#1f2a44;gap:8px}
.sponsor .sq{width:14px;height:14px;background:#1f2a44}

/* footer */
.footer{position:absolute;left:0;top:2669px;width:1200px;height:258px;background:var(--black)}
.footer h3{position:absolute;top:56px;color:var(--yellow);font-family:"Josefin Sans",sans-serif;font-weight:700;font-size:17px;text-transform:uppercase}
.fsq{position:absolute;top:99px;width:34px;height:34px}
.copy{position:absolute;top:212px;left:0;width:1200px;text-align:center;font-size:11px;color:#aaa}
.copy b{color:var(--yellow);font-weight:400}
</style>
</head>
<body>

<header class="hero">
  <div class="hero-photo" role="img" aria-label="Photo of a speaker presenting on a dark conference stage"></div>
  <div class="brand"><span class="brand-dot"></span>PKO.LV</div>
  <div class="btn-top" style="left:828px;width:103px">Login</div>
  <div class="btn-top register" style="left:944px;width:126px">Register</div>
  <nav class="nav">
    <a href="#" style="margin-right:52px">About</a>
    <a href="#" style="margin-right:52px">Venue</a>
    <a href="#" style="margin-right:52px">Speakers</a>
    <a href="#" style="margin-right:52px">Schedule</a>
    <a href="#" style="margin-right:52px">Talks</a>
    <a href="#">2012</a>
  </nav>
  <div class="dots"><span></span><span class="on"></span><span></span></div>
  <div class="countdown"><div>165<br>DAYS</div><div>11<br>HOURS</div><div>14<br>MINUTES</div></div>
  <div class="welcome">
    <h1 class="head">Welcome to Tolvik Code Meet</h1>
    <p>Dolore magnaorem ipsum dolor ser adipiscing elit, sed diam nonummy nibh euismod tincidunt ut laoreet dolore set.sit amet consectetuer Aadipiscing elit, sed diam nonummy. nonummy...</p>
  </div>
</header>

<main>
  <h2 class="head abs" style="left:131px;top:636px;font-size:16px">Latest News</h2>
  <div class="news-item" style="top:673px"><div class="date"><b>15</b><i>JULY</i></div><p>Dolore magnaorem ipsum dolor ser adipiscing elit, sed diam nonummy nibh euis-</p></div>
  <div class="news-item" style="top:775px"><div class="date"><b>29</b><i>JULY</i></div><p>Dolore magnaorem ipsum dolor ser adipiscing elit, sed diam nonummy nibh euis-</p></div>
  <div class="news-item" style="top:876px"><div class="date"><b>05</b><i>JULY</i></div><p>Dolore magnaorem ipsum dolor ser adipiscing elit, sed diam nonummy nibh euis-</p></div>
  <div class="news-item" style="top:977px"><div class="date"><b>15</b><i>JULY</i></div><p>Dolore magnaorem ipsum dolor ser adipiscing elit, sed diam nonummy nibh euis-</p></div>

  <h2 class="head abs" style="left:425px;top:636px;font-size:16px">Announcements</h2>
  <div class="arrows"><span></span><span></span></div>
  <article class="card" style="left:425px">
    <div class="pic" role="img" aria-label="Photo of the conference audience seated in a hall" style="background:linear-gradient(150deg,#6b5a4c,#2a2420)"></div>
    <h4>22 - 24 OCTOBER 2014</h4>
    <h5>Dravik, Kessel Bay, Norland</h5>
    <p>Dolore magnaorem ipsum dolor ser adipiscing elit, sed diam nonummy nibh euismod tincidunt ut</p>
    <span class="btn-yellow">Read more</span>
  </article>
  <article class="card" style="left:761px">
    <div class="pic" role="img" aria-label="Photo of attendees gathered at a sponsor booth" style="background:linear-gradient(150deg,#3b4f6e,#1f2533 60%,#6b5a3c)"></div>
    <h4>22 - 24 OCTOBER 2014</h4>
    <h5>Dravik, Kessel Bay, Norland</h5>
    <p>Dolore magnaorem ipsum dolor ser adipiscing elit, sed diam nonummy nibh euismod tincidunt ut</p>
    <span class="btn-yellow">Read more</span>
  </article>

  <section class="schedule">
    <h2 class="section-title head" style="top:43px">Schedule Information</h2>
    <div class="tabs">
      <span class="on">September 16, 2013</span><span>September 16, 2014</span><span>September 16, 2011</span><span>By Speaker</span>
    </div>
    <div class="timeline"></div>
    <div class="time" style="top:191px">09:00 am - 10:00 am</div><div class="knob" style="top:203px"></div>
    <div class="slot" style="top:179px;height:185px">
      <h4>The conference was organised by Latvian PKO User Group and Quarnex at Nov</h4>
      <div class="org">PKO.LV</div>
      <p>Dolore magnaorem ipsum dolor ser adipiscing elit, sed diam nonummy nibh euismod tincidunt ut laoreet dolore set.sit amet consectetuer Aadipiscing elit, sed diam nonummy. nonummy...Dolore magnaorem ipsum dolor ser adipiscing elit, sed diam nonummy nibh euismod tincidunt ut laoreet dolore set.sit amet consectetuer Aadipiscing elit, sed diam nonummy. nonummy...Dolore magnaorem ipsum dolor ser adipiscing elit, sed diam nonummy nibh</p>
    </div>
    <div class="time" style="top:388px">09:00 am - 10:00 am</div><div class="knob" style="top:400px"></div>
    <div class="slot" style="top:376px;height:61px"><h4>The conference was organised by Latvian PKO User Group and Quarnex at Nov</h4></div>
    <div class="time" style="top:461px">09:00 am - 10:00 am</div><div class="knob" style="top:473px"></div>
    <div class="slot" style="top:450px;height:61px"><h4>The conference was organised by Latvian PKO User Group and Quarnex at Nov</h4></div>
  </section>

  <h2 class="section-title head" style="top:1715px">Speakers Info</h2>
  <span class="side-arrow" style="left:100px"></span>
  <span class="side-arrow" style="left:1081px"></span>
  <div class="speaker" style="left:131px"><div class="face" role="img" aria-label="Speaker portrait"></div><h4>Arlen Vosk</h4><p>"Neque porro quisquam est qui dolorem ipsum quia dolor sit amet, consectetur, adipisci velit..."</p><div class="social"><span></span><span></span><span></span></div></div>
  <div class="speaker" style="left:380px"><div class="face" role="img" aria-label="Speaker portrait"></div><h4>Arlen Vosk</h4><p>"Neque porro quisquam est qui dolorem ipsum quia dolor sit amet, consectetur, adipisci velit..."</p><div class="social"><span></span><span></span><span></span></div></div>
  <div class="speaker active" style="left:624px"><div class="face" role="img" aria-label="Speaker portrait" style="background:linear-gradient(160deg,#cfd6c8,#6c7060)"></div><h4>Arlen Vosk</h4><p>"Neque porro quisquam est qui dolorem ipsum quia dolor sit amet, consectetur, adipisci velit..."</p><div class="social"><span></span><span></span><span></span></div></div>
  <div class="speaker" style="left:866px"><div class="face" role="img" aria-label="Speaker portrait"></div><h4>Arlen Vosk</h4><p>"Neque porro quisquam est qui dolorem ipsum quia dolor sit amet, consectetur, adipisci velit..."</p><div class="social"><span></span><span></span><span></span></div></div>

  <section class="photos">
    <span class="pill" style="left:131px;top:42px;font-weight:400;color:#777">Highlights</span>
    <span class="pill" style="left:199px;top:42px">All photos</span>
    <h2 class="section-title head" style="top:47px">Our Photos</h2>
    <p class="abs" style="left:0;width:1200px;top:83px;text-align:center;font-size:11px;color:var(--muted);font-style:italic">122 photos . Shared Publicly . July 7,2014</p>
    <span class="pill" style="left:863px;top:42px">Tag people</span>
    <span class="pill" style="left:948px;top:42px;width:64px;justify-content:center">Share</span>
    <span class="pill" style="left:1035px;top:42px;width:34px;justify-content:center">
      <svg width="10" height="6" viewBox="0 0 10 6"><path d="M1 1l4 4 4-4" fill="none" stroke="#333" stroke-width="1.5"/></svg>
    </span>
    <div class="photo" style="left:131px;background:linear-gradient(140deg,#2e4f7a,#c8742e 60%,#d8d3c8)" role="img" aria-label="Photo of a robot kit on a workshop table"></div>
    <div class="photo" style="left:367px;background:linear-gradient(140deg,#3a3330,#a7a39a 70%)" role="img" aria-label="Photo of attendees talking by a window"></div>
    <div class="photo" style="left:603px;background:linear-gradient(140deg,#d9d6cc,#5b3c33 55%,#2a2626)" role="img" aria-label="Photo of a speaker presenting in front of a screen"></div>
    <div class="photo" style="left:839px;background:linear-gradient(140deg,#7a2024,#c44a2a 50%,#332323)" role="img" aria-label="Photo of event staff in orange shirts"></div>
  </section>

  <h2 class="section-title head" style="top:2524px">Event Sponsors</h2>
  <span class="side-arrow" style="left:101px;top:2587px"></span>
  <span class="side-arrow" style="left:1081px;top:2587px"></span>
  <div class="sponsor" style="left:132px"><span class="sq"></span>Ovrenta</div>
  <div class="sponsor" style="left:330px">BRALMO</div>
  <div class="sponsor" style="left:486px">tirvex</div>
  <div class="sponsor" style="left:633px">Kelmora</div>
  <div class="sponsor" style="left:776px">quiply</div>
  <div class="sponsor" style="left:918px"><span class="sq"></span>Venlo Fin</div>
</main>

<footer class="footer">
  <h3 style="left:131px">Organized by:</h3>
  <div class="abs" style="left:131px;top:98px;color:var(--white);font-family:'Josefin Sans',sans-serif;font-weight:700;font-size:24px">TRZAP</div>
  <div class="abs" style="left:276px;top:98px;width:36px;height:36px;background:#eee"></div>
  <h3 style="left:486px">Follow us:</h3>
  <div class="fsq" style="left:486px;background:#3b5998"></div>
  <div class="fsq" style="left:536px;background:#e0548a"></div>
  <div class="fsq" style="left:586px;background:#45a7dc"></div>
  <div class="fsq" style="left:636px;background:#5b7b9a"></div>
  <div class="fsq" style="left:686px;background:#d65244"></div>
  <h3 style="left:833px">Newsletter</h3>
  <div class="abs" style="left:833px;top:99px;width:200px;height:34px;background:#1e1e1e;color:#777;font-size:11px;font-style:italic;padding:11px 12px">Enter email for newsletter</div>
  <div class="abs" style="left:1033px;top:99px;width:36px;height:34px;background:var(--yellow);display:flex;align-items:center;justify-content:center">
    <svg width="10" height="12" viewBox="0 0 10 12"><path d="M2 1l6 5-6 5z" fill="#111"/></svg>
  </div>
  <p class="copy">Copyright © 2014 <b>Tolvik Code Meet</b> All rights reserved. Terms of Use | Privacy Policy</p>
</footer>

</body>
</html>
```